Verdant Banner Design

We need 3 Banners for our superfood supplement e-commerce store.

1. Banner that advertises the food combining chart Dimensions 417 × 464 https://verdantlift.net/content/11-food-combining-rules

2. We need a banner that advertises our subscription program. (Dimensions 388 × 219)

3. We need a banner that highlights our ingredients. (Dimensions 388 × 215)

Our website: https://verdantlift.net/

1. The sizes are in dimensions.

2. Yes the banners are for our website, replacing the ones on the front page now https://verdantlift.net/

Content of Banners

1. Advertisng the food combining chart.

2. Advertising our Subscription program.

3 Advertising our ingredients.

Just use words like:

"Combine the right foods"

Target Market(s)

Organic Superfood Supplement

Contact Information for Business Card

The Business card has to be double sided and must have our logo

Colors

Designer to choose colors to be used in the design.

Requirements
Must have
• 1. You can use the attached images or not, it is up to you, please be creative.
• 2. Please provide the Raw AI files, and also give it in the following formats: JPEG, PNG,
• 3. I have added a file in the brief called subscription image please use to get an idea of the type of banner we are looking for, of course using our product images
Nice to have
• 1. Please show business card design as well, this will help us decide to choose you.
• 2. Please read the ingredients on the product itself, and if you can use some images for the ingredient banner that would be good.
• 3. The business card should have the following:
• Name: Rupert Halvey
• Title: Co-Founder
• Address: Harwick, VT
• Logo (see attached)
• Phone #: 855-640-3918
• Mobile #: 646-508-2274
• Email: info@verdantlift.net
• Website: www.verdantlift.net
Should not have
• No meat or dairy products in your images

```html
<!DOCTYPE html>
<html lang="en">
<head>
<meta charset="utf-8">
<title>Verdant Lift – Business Card</title>
<link href="https://fonts.googleapis.com/css2?family=Montserrat:wght@300;400;600;700&display=swap" rel="stylesheet">
<style>
  :root {
    --backdrop: #26282c;
    --card: #ffffff;
    --brand-red: #d71f26;
    --brand-green: #3f9142;
    --lime: #95c93d;
    --gold: #c39a35;
    --ink-grey: #555555;
    --shadow: rgba(0,0,0,0.45);
  }
  html, body {
    margin: 0;
    width: 1200px;
    height: 1200px;
    overflow: hidden;
    background: var(--backdrop);
    font-family: "Montserrat", sans-serif;
  }
  .canvas {
    position: relative;
    width: 1200px;
    height: 1200px;
  }
  .card {
    position: absolute;
    left: 150px;
    width: 900px;
    height: 514px;
    background: var(--card);
    box-shadow: 0 14px 30px var(--shadow);
    overflow: hidden;
  }
  .card--front { top: 50px; }
  .card--back { top: 636px; }
  .card svg { position: absolute; inset: 0; width: 100%; height: 100%; }

  .brand {
    position: absolute;
    display: flex;
    flex-direction: column;
  }
  .brand__row { display: flex; align-items: center; gap: 12px; }
  .brand__mark { width: 26px; height: 26px; background: var(--brand-green); }
  .brand__name {
    font-weight: 700;
    font-size: 50px;
    color: var(--brand-green);
    line-height: 1;
    letter-spacing: -0.5px;
  }
  .brand__tagline {
    margin: 8px 0 0 38px;
    font-size: 13px;
    font-weight: 400;
    color: var(--ink-grey);
  }
  .card--front .brand { left: 230px; top: 70px; }
  .card--back .brand { left: 230px; top: 110px; }

  .contact {
    position: absolute;
    left: 150px;
    top: 290px;
    margin: 0;
    padding: 0;
    list-style: none;
    color: #ffffff;
    font-size: 20px;
    font-weight: 300;
    line-height: 1.35;
  }
  .contact li { display: flex; align-items: center; gap: 8px; }
  .contact svg { position: static; width: 16px; height: 16px; flex: none; }
  .contact .indent { padding-left: 24px; }

  .person {
    position: absolute;
    left: 565px;
    top: 285px;
  }
  .person__name {
    margin: 0;
    font-size: 28px;
    font-weight: 600;
    color: var(--brand-red);
    letter-spacing: 0.5px;
  }
  .person__title {
    margin: 4px 0 0;
    font-size: 24px;
    font-weight: 300;
    color: var(--ink-grey);
    letter-spacing: 0.5px;
  }
</style>
</head>
<body>
<main class="canvas">

  <section class="card card--front" aria-label="Business card front">
    <svg viewBox="0 0 900 514" aria-hidden="true">
      <polygon class="accent-green" points="0,214 446,236 540,514 0,514" fill="var(--lime)"/>
      <polygon class="accent-red" points="0,228 432,250 522,514 0,514" fill="var(--brand-red)"/>
    </svg>

    <div class="brand">
      <div class="brand__row">
        <span class="brand__mark"></span>
        <span class="brand__name">Verdant Lift</span>
      </div>
      <span class="brand__tagline">Whole Plant Fuel For Modern Living</span>
    </div>

    <ul class="contact">
      <li>
        <svg viewBox="0 0 16 16"><path d="M8 1a5 5 0 0 0-5 5c0 4 5 9 5 9s5-5 5-9a5 5 0 0 0-5-5zm0 7a2 2 0 1 1 0-4 2 2 0 0 1 0 4z" fill="#fff"/></svg>
        : Harwick, VT
      </li>
      <li>
        <svg viewBox="0 0 16 16"><path d="M4 1l3 3-2 2c1 2 3 4 5 5l2-2 3 3-2 3C7 15 1 9 1 3z" fill="#fff"/></svg>
        : 855-640-3918
      </li>
      <li class="indent">646-508-2274</li>
      <li>
        <svg viewBox="0 0 16 16"><circle cx="8" cy="8" r="6.5" fill="none" stroke="#fff" stroke-width="1.5"/><path d="M1.5 8h13M8 1.5c3 3 3 10 0 13M8 1.5c-3 3-3 10 0 13" fill="none" stroke="#fff" stroke-width="1.2"/></svg>
        : www.verdantlift.net
      </li>
      <li>
        <svg viewBox="0 0 16 16"><rect x="1" y="3" width="14" height="10" fill="#fff"/><path d="M1 3l7 6 7-6" fill="none" stroke="var(--brand-red)" stroke-width="1.3"/></svg>
        : info@verdantlift.net
      </li>
    </ul>

    <div class="person">
      <p class="person__name">RUPERT HALVEY</p>
      <p class="person__title">CO-FOUNDER</p>
    </div>
  </section>

  <section class="card card--back" aria-label="Business card back">
    <svg viewBox="0 0 900 514">
      <defs>
        <linearGradient id="hero-tones" x1="0" y1="0" x2="1" y2="1">
          <stop offset="0" stop-color="var(--gold)"/>
          <stop offset="0.45" stop-color="var(--brand-red)"/>
          <stop offset="0.7" stop-color="var(--lime)"/>
          <stop offset="1" stop-color="var(--brand-green)"/>
        </linearGradient>
      </defs>
      <polygon class="swoosh" points="50,230 470,470 440,470" fill="var(--brand-red)"/>
      <polygon class="base-red" points="0,260 470,470 470,514 0,514" fill="var(--brand-red)"/>
      <polygon class="base-green" points="470,514 470,470 900,250 900,514" fill="var(--lime)"/>
      <polygon class="hero-illustration" role="img" aria-label="Illustration of a runner climbing a gold, red and green pyramid" points="420,420 880,150 760,514 470,514" fill="url(#hero-tones)"/>
    </svg>

    <div class="brand">
      <div class="brand__row">
        <span class="brand__mark"></span>
        <span class="brand__name">Verdant Lift</span>
      </div>
      <span class="brand__tagline">Whole Plant Fuel For Modern Living</span>
    </div>
  </section>

</main>
</body>
</html>
```